Travel agency website refresh

I want to refresh and simplify my current Wordpress.com website. Same general color scheme but modernize and make it user friendly for all devices. Must work with Wordpress. No live booking engines. We are a boutique luxury travel agency. Think luxury, vacation, boho chic, elegant, lush, tropical, cruises, first class. Romance and adventure.
Updates

Target Market(s)

Luxury travelers

Industry/Entity Type

Travel

Coding

Coded - Design and coding required

Number of Pages Required

5+ page

Font styles to use
Sans Serif

Colors
0094D4
00A9DD
6FCCEA
C7EBF8
E9F6FB

Requirements
Must have
• Compatible with Wordpress.com, homepage, about page, contact page, faq page
Nice to have
• The homepage should quickly tell the consumer the type of travel I specialize in. My current website has this (journeyswithmaren.example). I’d like to incorporate the about me as a preview on the home page.
Should not have
• Harsh colors, look generic

```html
<!DOCTYPE html>
<html lang="en">
<head>
<meta charset="utf-8">
<title>Journeys with Maren — Boutique Luxury Travel</title>
<link rel="stylesheet" href="https://fonts.googleapis.com/css2?family=Poppins:wght@300;400;500;600;700&display=swap">
<style>
  :root{
    --teal:#5ec4c9;
    --teal-dark:#48b2b8;
    --ink:#111418;
    --body:#7a7f85;
    --line:#e4e7ea;
    --white:#ffffff;
  }
  *{box-sizing:border-box;margin:0;padding:0}
  html,body{width:1200px;height:3931px;overflow:hidden;background:var(--white)}
  body{position:relative;font-family:"Poppins",sans-serif;color:var(--ink)}
  .abs{position:absolute}
  a{color:inherit;text-decoration:none}

  /* header */
  .brand{left:83px;top:28px;display:flex;align-items:center;gap:8px;font-weight:600;font-size:13px;color:var(--teal-dark);line-height:1.1}
  .brand-dot{width:26px;height:26px;border-radius:50%;background:var(--teal)}
  .nav{left:320px;top:38px;display:flex;gap:50px;font-size:16px;color:var(--body)}
  .nav .active{color:var(--teal);font-weight:500}
  .btn{display:flex;align-items:center;justify-content:center;background:var(--teal);color:var(--ink);font-weight:600}
  .btn-connect{left:991px;top:24px;width:126px;height:52px;font-size:17px}

  /* hero */
  .hero-title{left:83px;top:212px;width:470px;font-size:44px;font-weight:700;line-height:1.15}
  .hero-text{left:83px;top:382px;width:430px;font-size:12.5px;line-height:1.6;color:var(--body);text-align:justify}
  .btn-explore{left:83px;top:482px;width:128px;height:41px;font-size:16px}
  .hero-photo{left:575px;top:186px;width:542px;height:375px;background:linear-gradient(180deg,#5a87c8 0%,#9dbde6 38%,#2f6fa6 40%,#7fb3d0 58%,#d8d2c4 75%,#e8dcc8 100%)}

  /* services */
  .service{width:290px}
  .service-icon{width:52px;height:52px}
  .service h3{margin-top:20px;font-size:20px;font-weight:600}
  .service p{margin-top:10px;font-size:12.5px;line-height:1.6;color:var(--body);text-align:justify}
  .banner-photo{left:83px;top:878px;width:1034px;height:500px;background:linear-gradient(180deg,#4f86b8 0%,#a8c6dc 30%,#2c7a90 42%,#4fa7a8 62%,#c9b59a 80%,#b79f82 100%)}

  /* articles */
  .article-bar{left:83px;top:1503px;width:3px;height:252px;background:var(--teal)}
  .article{left:117px;width:417px}
  .article h3{font-size:27px;font-weight:600}
  .article p{margin-top:14px;font-size:16.5px;line-height:1.55;color:var(--body);text-align:justify}
  .article a{display:block;margin-top:20px;font-size:16px;font-weight:500;color:var(--teal)}
  .umbrella-photo{left:600px;top:1503px;width:517px;height:584px;background:linear-gradient(180deg,#7fb2e0 0%,#c5dcee 45%,#e79a3a 58%,#3fc0c6 75%,#b8ad9e 90%,#a99c8b 100%)}

  /* gallery */
  .gallery-title{left:0;width:1200px;top:2212px;text-align:center;font-weight:600}
  .gallery-title .small{font-size:27px;display:block}
  .gallery-title .big{font-size:35px;display:block;margin-top:6px}
  .credit{left:343px;top:2568px;display:flex;align-items:center;gap:8px;color:#fff}
  .credit .avatar{width:32px;height:32px;border-radius:50%;background:#d9d4cc;border:2px solid #fff}
  .credit b{font-size:13px;font-weight:500;display:block}
  .credit span{font-size:9px;opacity:.85}

  /* testimonials */
  .testi-title{left:83px;top:2962px;width:440px;font-size:35px;font-weight:700;line-height:1.45}
  .testi-text{left:83px;top:3124px;width:385px;font-size:16.5px;line-height:1.55;color:var(--body);text-align:justify}
  .btn-more{left:83px;top:3250px;width:162px;height:50px;font-size:16.5px}
  .card{top:2980px;width:502px;height:228px;background:#fff;box-shadow:0 6px 24px rgba(0,0,0,.08);padding:52px 28px 0}
  .card q{display:block;font-size:16.5px;font-weight:500;line-height:1.5;text-align:justify;quotes:"\201C" "\201D"}
  .card .who{margin-top:34px;text-align:right;font-size:13px}
  .arrow{width:24px;height:24px}

  /* booking */
  .book-title{left:83px;top:3400px;font-size:35px;font-weight:700}
  .book-text{left:83px;top:3452px;font-size:16.5px;color:var(--body)}
  .btn-book{left:855px;top:3412px;width:96px;height:51px;font-size:17px}
  .btn-learn{left:969px;top:3412px;width:148px;height:51px;font-size:17px;font-weight:600;color:var(--teal);border:2px solid var(--teal);display:flex;align-items:center;justify-content:center}

  /* footer */
  .footer-brand{left:95px;top:3700px;display:flex;align-items:center;gap:12px;font-size:30px;font-weight:600;color:#4a4f55}
  .footer-brand .mark{width:46px;height:46px;border-radius:50%;background:var(--teal)}
  .socials{left:84px;top:3790px;display:flex;gap:24px}
  .socials span{width:40px;height:40px;border-radius:50%;border:2px solid #bfe6e8;background:#eef9fa;display:flex;align-items:center;justify-content:center}
  .socials i{width:14px;height:14px;border-radius:3px;background:var(--teal);display:block}
  .fcol h4{font-size:20px;font-weight:600}
  .fcol ul{list-style:none;margin-top:20px}
  .fcol li{font-size:16.5px;color:var(--body);line-height:35px}
  .news p{margin-top:20px;font-size:11.5px;color:var(--body);line-height:1.5;width:200px}
  .news .input{margin-top:16px;width:208px;height:32px;background:#f4f5f6;border:1px solid var(--line);font-size:11px;color:var(--body);padding:8px 10px}
  .news .sub{margin-top:12px;width:208px;height:33px;font-size:11px;color:#fff}
  .rule{left:0;top:3876px;width:1200px;height:1px;background:var(--line)}
  .copy{left:0;width:1200px;top:3897px;text-align:center;font-size:13px;color:var(--body)}
</style>
</head>
<body>

<header>
  <a class="abs brand" href="#"><span class="brand-dot"></span><span>JOURNEYS<br>WITH MAREN</span></a>
  <nav class="abs nav">
    <a class="active" href="#">Home</a><a href="#">Why Us?</a><a href="#">Our Blog</a><a href="#">About Us</a><a href="#">Contact Us</a>
  </nav>
  <a class="abs btn btn-connect" href="#">Connect</a>
</header>

<section class="hero">
  <h1 class="abs hero-title">Explore The World<br>With Journeys<br>with Maren</h1>
  <p class="abs hero-text">Discover unique travel experiences crafted with passion and expertise. Whether you're dreaming of a romantic getaway, an adventurous expedition, or a relaxing retreat, we have the perfect itinerary for you.</p>
  <a class="abs btn btn-explore" href="#">Explore</a>
  <div class="abs hero-photo" role="img" aria-label="Two travellers sitting on a sandy beach facing a blue sea"></div>
</section>

<section class="services">
  <div class="abs service" style="left:83px;top:652px">
    <svg class="service-icon" viewBox="0 0 52 52"><path fill="#5ec4c9" d="M44 8c3-3 6-1 3 3L38 20l4 20-4 3-8-16-8 8 1 7-3 3-4-8-8-4 3-3 7 1 8-8-16-8 3-4 20 4z"/></svg>
    <h3>Custom Travel</h3>
    <p>Our personalized trips crafted to your preferences for unique and unforgettable adventures.</p>
  </div>
  <div class="abs service" style="left:458px;top:652px">
    <svg class="service-icon" viewBox="0 0 52 52" fill="#5ec4c9"><circle cx="26" cy="12" r="5"/><circle cx="12" cy="17" r="4"/><circle cx="40" cy="17" r="4"/><path d="M20 22h12l-2 22h-8z"/><path d="M6 24l8 2-2 16h-4z"/><path d="M46 24l-8 2 2 16h4z"/></svg>
    <h3>Family Vacations</h3>
    <p>Enjoyable and stress-free vacations with activities for all ages, perfect for family bonding.</p>
  </div>
  <div class="abs service" style="left:833px;top:652px">
    <svg class="service-icon" viewBox="0 0 52 52"><path fill="#5ec4c9" d="M26 46C10 34 4 26 4 17 4 10 10 5 16 5c4 0 8 2 10 6 2-4 6-6 10-6 6 0 12 5 12 12 0 9-6 17-22 29z"/><path fill="#fff" d="M32 40c-6-4-9-8-9-12 0-3 2-5 5-5 2 0 3 1 4 2 1-1 2-2 4-2 3 0 5 2 5 5 0 4-3 8-9 12z"/></svg>
    <h3>Honeymoon and Romance</h3>
    <p>Romantic escapes designed for couples, ideal for honeymoons, anniversaries, or special moments.</p>
  </div>
  <div class="abs banner-photo" role="img" aria-label="A couple holding hands on a beach beside turquoise water and rocky cliffs"></div>
</section>

<section class="articles">
  <div class="abs article-bar"></div>
  <article class="abs article" style="top:1503px">
    <h3>All-Inclusives</h3>
    <p>It can be difficult to properly budget for a vacation, especially when you factor in the (unknown) costs of essential elements like meals and entertainment.</p>
    <a href="#">Read More</a>
  </article>
  <article class="abs article" style="top:1712px">
    <h3>The Adventure Mindset</h3>
    <p>Nobody loves standing in long security lines, and I don't know one person who is thrilled by the fact that most airline seats only recline about four inches.</p>
    <a href="#">Read More</a>
  </article>
  <article class="abs article" style="top:1921px">
    <h3>The Caribbean Is Calling</h3>
    <p>Swaying in a hammock between two tall palms. Savoring a pampering morning at a seaside spa or an afternoon on a golf course.</p>
    <a href="#">Read More</a>
  </article>
  <div class="abs umbrella-photo" role="img" aria-label="Orange beach umbrellas over turquoise lounge chairs on the sand"></div>
</section>

<section class="gallery">
  <h2 class="abs gallery-title"><span class="small">Gallery Of</span><span class="big">Journeys with Maren</span></h2>
  <div class="abs" style="left:83px;top:2352px;width:225px;height:270px;background:linear-gradient(180deg,#c9a24e,#6b4a2c 60%,#3c3a2c)" role="img" aria-label="A-frame cabin in an autumn forest"></div>
  <div class="abs" style="left:325px;top:2352px;width:466px;height:270px;background:linear-gradient(135deg,#8fae5a,#b8c6a0 45%,#6d6a7c)" role="img" aria-label="Two hikers reading a map on a picnic blanket"></div>
  <div class="abs credit"><span class="avatar"></span><div><b>Theo Marsh</b><span>Mount Bromo</span></div></div>
  <div class="abs" style="left:808px;top:2352px;width:309px;height:270px;background:linear-gradient(180deg,#b8b5ad,#8a7d6c 55%,#5e4e3e)" role="img" aria-label="People relaxing on a busy beach"></div>
  <div class="abs" style="left:83px;top:2639px;width:173px;height:213px;background:linear-gradient(180deg,#dedad3,#b9aa98)" role="img" aria-label="Woman sitting on white sand"></div>
  <div class="abs" style="left:272px;top:2639px;width:284px;height:213px;background:linear-gradient(180deg,#dfe6ea,#9aa7b0 60%,#4e5a68)" role="img" aria-label="Family playing together on the beach"></div>
  <div class="abs" style="left:572px;top:2639px;width:356px;height:213px;background:linear-gradient(180deg,#cdd2d0,#8c7a5c 55%,#6a5440)" role="img" aria-label="Family walking along a wooden boardwalk"></div>
  <div class="abs" style="left:944px;top:2639px;width:173px;height:213px;background:linear-gradient(180deg,#49b9c6,#1c8ea3)" role="img" aria-label="Aerial view of swimmers in turquoise water"></div>
</section>

<section class="testimonials">
  <h2 class="abs testi-title">What People Say<br>About Journeys<br>with Maren</h2>
  <p class="abs testi-text">Discover why our clients love traveling with us. Hear their stories and experiences, and see how we've created unforgettable journeys for travelers around the world.</p>
  <a class="abs btn btn-more" href="#">Explore More</a>
  <div class="abs card" style="left:533px"><q>Our custom trip to Italy was incredible! Every detail was perfectly planned, making our experience seamless and memorable. Highly recommend!</q><div class="who">- Lena K.</div></div>
  <div class="abs card" style="left:1065px"><q>Our custom trip to Italy was incredible! Every detail was perfectly planned, making our experience seamless and memorable. Highly recommend!</q><div class="who">- Lena K.</div></div>
  <svg class="abs arrow" style="left:1031px;top:3248px" viewBox="0 0 24 24"><path d="M15 5l-7 7 7 7" fill="none" stroke="#7a7f85" stroke-width="2"/></svg>
  <svg class="abs arrow" style="left:1091px;top:3248px" viewBox="0 0 24 24"><path d="M9 5l7 7-7 7" fill="none" stroke="#111418" stroke-width="2"/></svg>
</section>

<section class="booking">
  <h2 class="abs book-title">Book Now at Journeys with Maren</h2>
  <p class="abs book-text">Ready for adventure? Book now with Journeys with Maren for your perfect trip!</p>
  <a class="abs btn btn-book" href="#">Book</a>
  <a class="abs btn-learn" href="#">Learn More</a>
</section>

<footer>
  <div class="abs footer-brand"><span class="mark"></span><span>MAREN</span></div>
  <div class="abs socials"><span><i></i></span><span><i></i></span><span><i></i></span><span><i></i></span></div>
  <div class="abs fcol" style="left:417px;top:3630px"><h4>Other Pages</h4><ul><li>About</li><li>Contact</li><li>Services</li><li>Booking</li><li>Help</li></ul></div>
  <div class="abs fcol" style="left:642px;top:3630px"><h4>Quick Links</h4><ul><li>Privacy Policy</li><li>Terms Of Service</li><li>Disclaimer</li><li>Credits</li><li>FAQ</li></ul></div>
  <div class="abs fcol news" style="left:881px;top:3630px"><h4>Newsletter</h4><p>Lorem ipsum dolor sit amet, consectetur adipiscing elit.</p><div class="input">Your email</div><div class="btn sub">Subscribe</div></div>
  <div class="abs rule"></div>
  <p class="abs copy">©2024 Journeys with Maren. All rights reserved.</p>
</footer>

</body>
</html>
```